Web design - holistic filmmaker

I need a design for my new website.

I am a holistic filmmaker, ie I make films for healers, alternative practitioners, spiritual people and institutions that offer training in this field.

The design should be noble, bright, convey the feeling of space and expanse and have some particularly beautiful color accents.

The structure is: start page, offer, references, about me, imprint.

As an idea for the start page, I thought that either I could introduce myself as a filmmaker and my offer, or we could start right on the start page with the references, ie photos and links to already realized projects.

If you want more information or an exchange, I'd love to hear from you. At the moment I just don't know how to describe it better.

The winner will then be asked to design a logo.

Target Market(s)

healers, alternative practitioners, spiritual people and institutions that offer training in this field

Industry/Entity Type

Film production

Number of Pages Required

3 page

```html
<!DOCTYPE html>
<html lang="en">
<head>
<meta charset="utf-8">
<title>Lumenreel — Holistic Filmmaking</title>
<link rel="stylesheet" href="https://fonts.googleapis.com/css2?family=Oswald:wght@500;700&family=Roboto:wght@300;400;500;700&display=swap">
<style>
  :root {
    --accent: #ffbb00;
    --ink: #2b2b2b;
    --text: #555555;
    --white: #ffffff;
  }
  * { margin: 0; padding: 0; box-sizing: border-box; }
  html, body { width: 1200px; height: 1200px; overflow: hidden; background: var(--white); }
  body { position: relative; font-family: "Roboto", sans-serif; }

  .hero { position: absolute; left: 0; top: 0; width: 1200px; height: 530px; overflow: hidden; }
  .hero-photo {
    position: absolute; inset: 0;
    background:
      radial-gradient(ellipse at 14% 40%, #f1d7a8 0%, rgba(226,188,130,0.6) 22%, transparent 50%),
      radial-gradient(ellipse at 72% 42%, #c98a52 0%, rgba(180,120,70,0.6) 30%, transparent 62%),
      radial-gradient(ellipse at 40% 95%, #8c7a6a 0%, transparent 55%),
      linear-gradient(120deg, #b99a74 0%, #8a6a4c 42%, #a06c40 70%, #5e5048 100%);
  }
  .hero-shade { position: absolute; inset: 0; background: rgba(38,26,14,0.32); }

  .site-header {
    position: absolute; left: 0; top: 0; width: 1200px; height: 78px;
    border-bottom: 1px solid rgba(255,255,255,0.3);
  }
  .brand {
    position: absolute; left: 30px; top: 21px;
    font-weight: 500; font-size: 28px; line-height: 34px;
    color: var(--white); display: flex; align-items: center; gap: 6px;
  }
  .brand-dot { width: 7px; height: 7px; background: var(--white); border-radius: 50%; }
  .main-nav { position: absolute; left: 362px; top: 25px; display: flex; gap: 42px; }
  .main-nav a {
    color: var(--white); text-decoration: none; font-weight: 700; font-size: 14px;
    padding-bottom: 6px; position: relative;
  }
  .main-nav a.active::after {
    content: ""; position: absolute; left: 0; right: 0; bottom: 0; height: 3px; background: var(--accent);
  }
  .menu-toggle { position: absolute; left: 1126px; top: 27px; width: 20px; }
  .menu-toggle span { display: block; height: 2px; background: var(--white); margin-bottom: 4px; }

  .hero-content { position: absolute; left: 0; top: 195px; width: 1200px; text-align: center; color: var(--white); }
  .hero-kicker { font-weight: 500; font-size: 14px; }
  .hero-title {
    font-family: "Oswald", sans-serif; font-weight: 700; font-size: 74px;
    letter-spacing: 1px; line-height: 1; margin-top: 16px;
  }
  .hero-text { font-weight: 300; font-size: 14px; line-height: 23px; width: 610px; margin: 16px auto 0; }
  .btn {
    display: inline-block; background: var(--accent); color: var(--white);
    font-weight: 700; font-size: 12px; letter-spacing: 2.5px; text-decoration: none; text-align: center;
  }
  .hero .btn { margin-top: 24px; width: 152px; height: 39px; line-height: 39px; letter-spacing: 2px; }

  .about { position: absolute; left: 133px; top: 636px; width: 920px; height: 264px; }
  .about-label { position: absolute; left: 0; top: 0; color: var(--accent); font-size: 14px; }
  .about-title {
    position: absolute; left: 0; top: 28px;
    font-family: "Oswald", sans-serif; font-weight: 500; font-size: 37px; color: var(--ink);
  }
  .about-text {
    position: absolute; left: 0; top: 96px; width: 446px;
    font-weight: 300; font-size: 14px; line-height: 22px; color: var(--text); letter-spacing: 0.3px;
  }
  .about .btn { position: absolute; left: 0; top: 181px; width: 137px; height: 42px; line-height: 42px; }
  .about-photo {
    position: absolute; left: 480px; top: 0; width: 439px; height: 264px;
    background:
      radial-gradient(ellipse at 68% 30%, #d9c39a 0%, transparent 42%),
      radial-gradient(ellipse at 25% 85%, #9a8266 0%, transparent 50%),
      linear-gradient(180deg, #5a4a38 0%, #6e5a44 60%, #7d6650 100%);
  }

  .production-head {
    position: absolute; left: 0; top: 1005px; width: 1200px;
    display: flex; justify-content: center; align-items: center; gap: 18px;
  }
  .production-head .rule { width: 70px; height: 3px; background: var(--accent); }
  .production-head h2 {
    font-family: "Oswald", sans-serif; font-weight: 700; font-size: 50px; color: var(--ink); line-height: 1;
  }
  .production-icons { position: absolute; left: 0; top: 1153px; width: 1200px; height: 47px; }
  .production-icons svg { position: absolute; top: 0; width: 46px; height: 46px; }
</style>
</head>
<body>
  <section class="hero">
    <div class="hero-photo" role="img" aria-label="Bright, warm photo of a filmmaker looking through a camera in soft golden light"></div>
    <div class="hero-shade"></div>

    <header class="site-header">
      <div class="brand">Lumenreel <span class="brand-dot"></span></div>
      <nav class="main-nav">
        <a class="active" href="#">Home</a>
        <a href="#">Offer</a>
        <a href="#">References</a>
        <a href="#">About Me</a>
        <a href="#">Imprint</a>
        <a href="#">Contact</a>
      </nav>
      <div class="menu-toggle"><span></span><span></span><span></span></div>
    </header>

    <div class="hero-content">
      <p class="hero-kicker">Holistic Films for Healers &amp; Teachers</p>
      <h1 class="hero-title">INNER LIGHT.</h1>
      <p class="hero-text">Films that give healers, practitioners and spiritual schools space to be seen, with calm images, honest voices and room to breathe.</p>
      <a class="btn" href="#">Watch Showreel</a>
    </div>
  </section>

  <section class="about">
    <p class="about-label">Basic Info About Me</p>
    <h2 class="about-title">ABOUT MY WORK</h2>
    <p class="about-text">I make films for healers, alternative practitioners and training institutes, so the depth of your work can reach the people who are looking for it.</p>
    <a class="btn" href="#">READ MORE</a>
    <div class="about-photo" role="img" aria-label="Photo of the filmmaker operating a video camera at an event"></div>
  </section>

  <section class="production">
    <div class="production-head">
      <span class="rule"></span>
      <h2>MY OFFER</h2>
      <span class="rule"></span>
    </div>
    <div class="production-icons">
      <svg style="left:201px" viewBox="0 0 46 46" fill="none" stroke="#2b2b2b" stroke-width="2.5">
        <rect x="2" y="8" width="42" height="26"/><line x1="14" y1="40" x2="32" y2="40"/>
      </svg>
      <svg style="left:451px" viewBox="0 0 46 46" fill="none" stroke="#2b2b2b" stroke-width="2.5">
        <path d="M12 4h22v12a11 11 0 0 1-22 0z"/><path d="M12 8H5a7 7 0 0 0 8 12"/><path d="M34 8h7a7 7 0 0 1-8 12"/>
        <line x1="23" y1="27" x2="23" y2="36"/><rect x="15" y="36" width="16" height="6"/><line x1="23" y1="10" x2="23" y2="17"/>
      </svg>
      <svg style="left:701px" viewBox="0 0 46 46" fill="none" stroke="#2b2b2b" stroke-width="2.5">
        <rect x="4" y="2" width="38" height="44"/><line x1="12" y1="2" x2="12" y2="46"/><line x1="34" y1="2" x2="34" y2="46"/>
        <path d="M8 8v2M8 16v2M8 24v2M8 32v2M8 40v2M38 8v2M38 16v2M38 24v2M38 32v2M38 40v2"/>
      </svg>
      <svg style="left:952px" viewBox="0 0 46 46" fill="none" stroke="#2b2b2b" stroke-width="2.5">
        <path d="M2 14h10l4-6h14l4 6h10v28H2z"/><circle cx="23" cy="27" r="8"/><line x1="6" y1="20" x2="12" y2="20"/>
      </svg>
    </div>
  </section>
</body>
</html>
```